We need UI/UX design for a public, informational website for The Copper Lantern.
The pages, structure, and content scope are already defined. Designers are required to work only on the UI/UX layout of these existing pages, focusing on clarity, hierarchy, spacing, and usability. Do not add, remove, rename, or reinterpret pages or content.
The website is strictly informational only. It must not include accounts, onboarding, payments, custody, escrow administration, marketplaces, dashboards, or any transactional functionality.
Scope of work
Apply UI/UX design to the predefined website pages
Design layout for text, images, notices, and sections
Ensure consistent components and layout patterns across page types
Optimize layouts for long form, compliance focused content
Content writing, page creation, and branding changes are out of scope.
Structure reference
The complete page list, hierarchy, and content definitions are provided in the technical documentation and must be treated as the primary source of truth.
A Figma link is provided only as a light visual reference for page existence and structure:
https://maple-kettle-48203917.plansite.example/
Designers must rely on the documentation for in depth and authoritative reference.
Brand guidelines
The Copper Lantern has existing brand guidelines and official logos, including light and dark versions. These assets will be provided and must be followed exactly. Designers must not redesign, alter, or reinterpret the brand identity.
Look and feel direction
The desired visual direction is inspired by:
https://quorvanta.example/
This reference is provided only to indicate:
Institutional and enterprise tone
Clean, modern typography
Strong hierarchy and generous whitespace
Editorial, content first layouts
Do not copy branding, layouts, components, or assets from the reference site.
Hero section direction
The hero section should follow a similar structural approach to the hero used on https://quorvanta.example/
, meaning:
Strong editorial framing
Clear headline hierarchy
Calm, institutional first impression
However, the background video must be Abu Dhabi focused, not generic or global. The video should visually reflect:
Abu Dhabi skyline or architectural language
Institutional, sovereign, long term infrastructure tone
Clean, slow, cinematic motion
No promotional, marketing, or lifestyle visuals
The hero must remain informational, restrained, and credible. No hype. No calls to invest. No implied participation.
Constraints
One global primary CTA only: “Continue to Brightmoor” (external)
All other interactions must be informational
No visuals or language implying offers, investment, eligibility, or participation
Clear separation between informational content and any external operational platforms
Deliverables
High fidelity UI/UX designs created in Figma, covering:
Desktop layouts
Tablet layouts where relevant
Mobile layouts
Complete Figma file(s) including:
All designed pages defined in the technical documentation
A reusable component library (headers, footers, cards, notice panels, forms, CTAs, typography styles, spacing system)
Clearly defined layout grids, spacing rules, and text styles
Proper use of components and variants, not detached frames
Designs prepared for developer handoff, including:
Clear layer naming and structure
Auto layout where appropriate
Consistent use of styles and components
Responsive behavior demonstrated within Figma
Notes or annotations only where necessary for clarity
No prototypes, interactions, or motion design beyond basic layout states, unless explicitly requested. The focus is static UI/UX clarity, not animation.
A detailed technical specification document and official brand assets will be provided.
Any designs delivered outside Figma, that alter structure or content, or that ignore the defined constraints, boundaries, or tone will be rejected.

```html
<!DOCTYPE html>
<html lang="en">
<head>
<meta charset="utf-8">
<title>The Copper Lantern</title>
<link href="https://fonts.googleapis.com/css2?family=Plus+Jakarta+Sans:wght@400;500;600;700;800&display=swap" rel="stylesheet">
<style>
:root{
  --navy:#0b1830;
  --navy-deep:#07111f;
  --blue:#1f9bd7;
  --purple:#6a3db4;
  --ink:#111827;
  --muted:#4b5563;
  --white:#ffffff;
  --line:rgba(255,255,255,.18);
}
*{box-sizing:border-box;margin:0;padding:0}
html,body{width:1200px;height:4212px;overflow:hidden}
body{position:relative;background:var(--white);color:var(--ink);font-family:"Plus Jakarta Sans",Arial,sans-serif}
.abs{position:absolute}
.btn{display:inline-block;background:var(--blue);color:var(--white);font-weight:600;font-size:15px;padding:13px 26px;border-radius:8px;text-decoration:none}
.h2{font-size:44px;font-weight:800;line-height:1.12;letter-spacing:-.5px}
.body{font-size:15px;line-height:1.6;color:var(--muted)}

/* navigation */
.site-nav{left:0;top:0;width:1200px;height:96px;background:var(--white);display:flex;align-items:center;padding:0 60px;justify-content:space-between;z-index:3}
.brand{display:flex;align-items:center;gap:10px;font-weight:700;font-size:20px;color:var(--navy)}
.brand-dot{width:34px;height:34px;border-radius:50%;background:var(--blue)}
.nav-links{display:flex;gap:34px;align-items:center;font-size:15px;font-weight:500;color:var(--ink)}
.nav-links span.has-menu::after{content:" ▾";font-size:11px}

/* hero */
.hero{left:0;top:96px;width:1200px;height:632px;border-radius:0 0 60px 60px;background:linear-gradient(180deg,#3c4b5e 0%,#26374c 45%,#14233a 100%);overflow:hidden}
.hero-title{left:90px;top:170px;font-size:64px;font-weight:800;line-height:1.1;color:var(--white);letter-spacing:-1px}
.hero-text{left:90px;top:260px;width:440px;font-size:15px;line-height:1.6;color:rgba(255,255,255,.9)}
.hero-cta{left:90px;top:460px}
.slider-bar{left:240px;top:540px;width:140px;height:14px;background:#2b45c7;border-radius:2px}
.notice-card{left:830px;top:250px;width:270px;background:var(--white);border-radius:16px;padding:12px;box-shadow:0 12px 30px rgba(0,0,0,.3)}
.notice-media{height:110px;border-radius:10px;background:linear-gradient(180deg,#8aa3bd,#3a4e66)}
.notice-card h3{font-size:18px;font-weight:700;margin:14px 4px 6px}
.notice-card p{font-size:13px;line-height:1.5;color:var(--muted);margin:0 4px 6px}

/* governance */
.origination-title{left:0;top:800px;width:1200px;text-align:center}
.origination-text{left:220px;top:920px;width:760px;text-align:center}
.photo{border-radius:10px;background:linear-gradient(180deg,#f08a3c 0%,#b9553a 45%,#3b3f55 100%)}

/* roles */
.circle-photo{border-radius:50%;background:linear-gradient(180deg,#f39a48 0%,#b34f3c 50%,#263449 100%)}
.roles-title{left:572px;top:1470px}
.roles-text{left:572px;top:1540px;width:440px}

/* ecosystem */
.ecosystem{left:0;top:1860px;width:1200px;height:640px;border-radius:60px 60px 0 0;background:linear-gradient(180deg,#0c1a34 0%,#15294a 60%,#2a3d5a 100%);color:var(--white);text-align:center}
.ecosystem .h2{margin-top:90px}
.ecosystem .lead{font-size:15px;color:rgba(255,255,255,.85);margin-top:10px}
.layers{display:flex;justify-content:center;gap:60px;margin-top:56px}
.layer{width:240px}
.layer h3{font-size:20px;font-weight:700;margin-bottom:8px}
.layer p{font-size:14px;line-height:1.55;color:rgba(255,255,255,.8)}
.ecosystem .note{width:720px;margin:56px auto 0;font-size:15px;line-height:1.6;color:rgba(255,255,255,.9)}
.ecosystem .btn{margin-top:40px}

/* escrow */
.escrow-title{left:140px;top:2640px}
.escrow-text{left:140px;top:2830px;width:440px}
.escrow-photo{left:640px;top:2600px;width:420px;height:380px;border-radius:30px;background:linear-gradient(180deg,#3d2b3e 0%,#d6643a 45%,#f29c54 60%,#3a3440 100%)}

/* operations */
.ops-photo{background:linear-gradient(180deg,#7ea6d6 0%,#cfa36e 55%,#3a4a5e 100%)}
.ops-title{left:560px;top:3100px}
.ops-text{left:560px;top:3218px;width:480px}
.ops-cta{left:560px;top:3400px}

/* footer */
.site-footer{left:0;top:3700px;width:1200px;height:512px;background:var(--navy-deep);color:var(--white)}
.contact-panel{left:100px;top:3540px;width:1000px;height:240px;border-radius:24px;background:var(--purple);color:var(--white);padding:54px 60px;z-index:2}
.contact-panel h2{font-size:40px;font-weight:800;letter-spacing:-.5px}
.contact-panel p{width:640px;margin-top:14px;font-size:15px;line-height:1.6;color:rgba(255,255,255,.9)}
.contact-circle{right:70px;top:60px;width:120px;height:120px;border-radius:50%;background:var(--white);color:var(--ink);display:flex;flex-direction:column;align-items:center;justify-content:center;font-size:16px;font-weight:700;line-height:1.2;text-align:center}
.footer-brand{left:100px;top:3990px;display:flex;align-items:center;gap:10px;font-weight:700;font-size:20px;color:var(--white)}
.footer-col{top:3860px;color:var(--white)}
.footer-col h4{font-size:18px;font-weight:700;margin-bottom:14px;color:var(--white)}
.footer-col li{list-style:none;font-size:14px;line-height:1.9;color:rgba(255,255,255,.85)}
.footer-notice p{width:280px;font-size:14px;line-height:1.6;color:rgba(255,255,255,.85)}
.footer-rule{left:100px;top:4130px;width:1000px;height:1px;background:var(--line)}
.copyright{left:0;top:4160px;width:1200px;text-align:center;font-size:13px;color:rgba(255,255,255,.75)}
</style>
</head>
<body>

<header class="site-nav abs">
  <div class="brand"><span class="brand-dot"></span>The Copper Lantern</div>
  <nav class="nav-links">
    <span>Home</span><span class="has-menu">Framework</span><span class="has-menu">Projects</span><span>Brightmoor</span><span class="has-menu">Insights</span><span class="has-menu">Company</span>
    <a class="btn" href="#">Contact Us</a>
  </nav>
</header>

<section class="hero abs" role="img" aria-label="Abu Dhabi skyline of glass towers at dusk">
  <h1 class="hero-title abs">The Copper Lantern</h1>
  <p class="hero-text abs">is a governance and project origination group. Its purpose is to define structural standards and oversight principles for complex initiatives that may involve multiple parties, staged execution, and long-term accountability. This website explains those standards and outlines how responsibilities are separated across governance, operations, and project execution.</p>
  <a class="btn hero-cta abs" href="#">Continue to Brightmoor</a>
  <div class="slider-bar abs"></div>
  <aside class="notice-card abs">
    <div class="notice-media" role="img" aria-label="City towers photograph"></div>
    <h3>This site is informational.</h3>
    <p>It does not provide onboarding, account access, eligibility checks, custody of funds, escrow administration, or transactional services.</p>
  </aside>
</section>

<h2 class="h2 origination-title abs">Governance and Project<br>Origination</h2>
<p class="body origination-text abs">Governance in this context refers to the standards that determine how projects are structured and how oversight is described. Origination refers to the initial design and definition of an initiative, including role separation, reporting expectations, and boundaries set before execution begins. The Copper Lantern focuses on these governance-level elements rather than on operating day-to-day workflows.</p>
<div class="photo abs" style="left:160px;top:1160px;width:280px;height:160px" role="img" aria-label="Skyline at sunset"></div>
<div class="photo abs" style="left:460px;top:1160px;width:280px;height:160px" role="img" aria-label="Towers along the waterfront at sunset"></div>
<div class="photo abs" style="left:760px;top:1160px;width:280px;height:160px" role="img" aria-label="Aerial city view at golden hour"></div>

<div class="circle-photo abs" style="left:200px;top:1440px;width:280px;height:280px" role="img" aria-label="Skyline at sunset framed in a circle"></div>
<h2 class="h2 roles-title abs">Clear Role Separations.</h2>
<p class="body roles-text abs">The ecosystem is designed around clear separation of responsibilities. Governance activities belong at the framework layer. Operational workflows, where available, belong on a separate operating platform designed for process execution and recordkeeping. Assets and project execution, where applicable, belong at the project level through ring-fenced structures created for specific initiatives. This separation is intended to reduce ambiguity and help stakeholders understand who is responsible for what.</p>

<section class="ecosystem abs" role="img" aria-label="Night city skyline behind the section">
  <h2 class="h2">How the Ecosystem Works</h2>
  <p class="lead">At a high level, the ecosystem can be understood as three layers.</p>
  <div class="layers">
    <div class="layer"><h3>Governance</h3><p>defines standards, explains role boundaries, &amp; publishes framework information.</p></div>
    <div class="layer"><h3>The ecosystem core</h3><p>Occurs at the project level through dedicated structures that hold responsibilities.</p></div>
    <div class="layer"><h3>Operations</h3><p>Manages workflow processes such as documentation steps &amp; record and tracked entitlements.</p></div>
  </div>
  <p class="note">This website focuses on the governance layer and provides links to learn about structural concepts such as role separation, escrow and milestone framing, and recordkeeping technology.</p>
  <a class="btn" href="#">Learn the Framework</a>
</section>

<h2 class="h2 escrow-title abs">Independent<br>Escrow &amp; Milestone<br>Oversight</h2>
<p class="body escrow-text abs">Some initiatives use independent escrow arrangements to coordinate staged releases linked to milestone completion. Escrow can support execution discipline by requiring defined evidence before releases occur. Escrow does not guarantee outcomes, timelines, or success, and it is not administered by this website operator. This site describes the concept for clarity and transparency.</p>
<div class="escrow-photo abs" role="img" aria-label="Skyline under a vivid sunset sky"></div>

<div class="circle-photo ops-photo abs" style="left:180px;top:3080px;width:320px;height:320px" role="img" aria-label="Waterfront towers in daylight framed in a circle"></div>
<h2 class="h2 ops-title abs">Where Operational<br>Workflows Happen</h2>
<p class="body ops-text abs">Operational workflows, including any onboarding or workflow participation where permitted, occur on a separate operating platform under separate terms and policies. If you need operational access, use the link on this site to navigate externally. This website does not host those workflows.</p>
<a class="btn ops-cta abs" href="#">Continue to Brightmoor</a>

<section class="contact-panel abs">
  <h2>Contact and Inquiries</h2>
  <p>If you have questions about governance framework concepts, role boundaries, or information published on this website, you can contact the team using the Contact page. Do not submit sensitive personal data through public forms.</p>
  <div class="contact-circle abs">
    <svg width="18" height="18" viewBox="0 0 18 18" aria-hidden="true"><path d="M4 14L14 4M6 4h8v8" fill="none" stroke="#111827" stroke-width="2"/></svg>
    Contact<br>Us
  </div>
</section>

<footer class="site-footer abs"></footer>
<div class="footer-brand abs"><span class="brand-dot"></span>The Copper Lantern</div>
<div class="footer-col abs" style="left:360px">
  <h4>Company</h4>
  <ul><li>Framework</li><li>Projects</li><li>Brightmoor</li><li>Insights</li><li>Company</li><li>Contact</li><li>Glossary</li></ul>
</div>
<div class="footer-col abs" style="left:580px">
  <h4>Legal</h4>
  <ul><li>Legal</li><li>Terms of Use</li><li>Privacy Policy</li><li>Cookie Policy</li><li>Disclaimer &amp; Risk Notices</li><li>Acceptable Use Policy</li><li>Accessibility Statement</li></ul>
</div>
<div class="footer-col footer-notice abs" style="left:820px">
  <h4>This site is informational.</h4>
  <p>This website is provided for general informational purposes only. Nothing on this site is an offer, solicitation, or professional advice.</p>
</div>
<div class="footer-rule abs"></div>
<p class="copyright abs">©2026 The Copper Lantern. All rights reserved.</p>

</body>
</html>
```